Need high-end luxury business cards with raised element of logo

Looking for a non-standard business card with the option of part of our logo elements to be printed as raised or embossed. Would like at least 5 different photos on the backside. Looking at printing through this: https://www.cardvelo.com/raised-spot-uv-business-cards.html

updated the logo file

```html
<!DOCTYPE html>
<html lang="en">
<head>
<meta charset="utf-8">
<title>Halvern Row – Business Card</title>
<link href="https://fonts.googleapis.com/css2?family=Montserrat:wght@400;500;700&display=swap" rel="stylesheet">
<style>
  :root {
    --backdrop: #2a2a2b;
    --slate: #3f6075;
    --slate-deep: #33505f;
    --ink: #2e2e33;
    --paper: #ffffff;
  }
  * { box-sizing: border-box; margin: 0; padding: 0; }
  html, body {
    width: 1200px; height: 1186px; overflow: hidden;
    background: var(--backdrop);
    font-family: "Montserrat", sans-serif;
  }
  .stage {
    width: 1200px; height: 1186px;
    display: flex; flex-direction: column;
    align-items: center; justify-content: center; gap: 56px;
  }
  .card {
    width: 900px; height: 514px;
    border-radius: 34px;
    position: relative; overflow: hidden;
  }
  .card--back {
    background: var(--slate);
    display: flex; align-items: center; justify-content: center; gap: 26px;
  }
  .card--back .brand-dot {
    width: 46px; height: 46px; border-radius: 50%;
    background: var(--slate-deep);
  }
  .card--back .brand-name {
    font-weight: 700; font-size: 84px; letter-spacing: 6px;
    color: var(--slate-deep);
  }
  .card--front {
    background: var(--paper);
    display: flex; align-items: center;
  }
  .front-brand {
    width: 470px; display: flex; align-items: center; justify-content: center;
  }
  .front-brand .brand-name {
    font-weight: 700; font-size: 50px; letter-spacing: 4px;
    color: var(--slate);
  }
  .divider {
    width: 2px; height: 250px; background: var(--slate);
  }
  .contact {
    padding-left: 40px; color: var(--ink);
  }
  .contact .person {
    font-weight: 700; font-size: 30px; color: var(--slate);
  }
  .contact .role {
    font-size: 17px; margin-top: 2px; margin-bottom: 20px;
  }
  .contact ul { list-style: none; }
  .contact li {
    display: flex; align-items: center; gap: 12px;
    font-size: 19px; line-height: 30px;
  }
  .contact li svg { width: 16px; height: 16px; fill: var(--ink); flex: none; }
  .contact .address {
    font-size: 19px; line-height: 26px; margin-top: 18px; padding-left: 28px;
  }
</style>
</head>
<body>
<main class="stage">
  <section class="card card--back" aria-label="Card back">
    <span class="brand-dot"></span>
    <span class="brand-name">HALVERN ROW</span>
  </section>

  <section class="card card--front" aria-label="Card front">
    <div class="front-brand">
      <span class="brand-name">HALVERN ROW</span>
    </div>
    <div class="divider"></div>
    <div class="contact">
      <p class="person">Dario Lenz</p>
      <p class="role">CEO &amp; Founder</p>
      <ul>
        <li>
          <svg viewBox="0 0 16 16" aria-hidden="true"><path d="M3 1h3l1.5 4-2 1.3a9 9 0 0 0 4.2 4.2L11 8.5l4 1.5v3a2 2 0 0 1-2 2A13 13 0 0 1 1 3a2 2 0 0 1 2-2z"/></svg>
          955 41 27 83
        </li>
        <li>
          <svg viewBox="0 0 16 16" aria-hidden="true"><path d="M1 3h14v10H1z M1 3l7 6 7-6" stroke="#fff" stroke-width="1.2"/></svg>
          info@halvernrow.com
        </li>
        <li>
          <svg viewBox="0 0 16 16" aria-hidden="true"><circle cx="8" cy="8" r="7"/><path d="M1 8h14M8 1c3 3 3 11 0 14M8 1c-3 3-3 11 0 14" stroke="#fff" stroke-width="1" fill="none"/></svg>
          www.halvernrow.com
        </li>
      </ul>
      <p class="address">Pol. Ind. Norte, C/3 nº 12<br>41500 Villanueva del Río</p>
    </div>
  </section>
</main>
</body>
</html>
```